Kestrel Forge Tech
Bus. Cards/Stationary/Presentation
Kestrel Forge Tech - Information Technology
Creative Brief
Use specific fonts
Open to ideas on font pairing
Professional
Wendell Pask
Owner
218 Larkspur Avenue Suite 4400 Harlow Bend, OR 97915
Wendell.Pask@kestrelforgetech.com
www.kestrelforgetech.com
I am open to my logo displayed on the back. I am also open to ideas on the back of business card. Be creative on front and back.

```html
<!DOCTYPE html>
<html lang="en">
<head>
<meta charset="utf-8">
<title>Kestrel Forge Tech — Business Cards</title>
<link rel="stylesheet" href="https://fonts.googleapis.com/css2?family=Open+Sans:wght@400;600;700&display=swap">
<style>
  :root {
    --backdrop: #3a3735;
    --card-light: #f4f4f4;
    --card-light-edge: #dcdcdc;
    --card-dark: #2f2f2f;
    --card-dark-edge: #444444;
    --brand-green: #7cc242;
    --ink-dark: #4a4a4a;
    --ink-light: #e6e6e6;
    --ink-muted: #8a8a8a;
    --mark-grey: #8c8c8c;
  }
  * { box-sizing: border-box; margin: 0; padding: 0; }
  html, body {
    width: 1200px; height: 851px; overflow: hidden;
    background: var(--backdrop);
    font-family: "Open Sans", Arial, sans-serif;
  }
  .sheet { position: relative; width: 1200px; height: 851px; }

  .card {
    position: absolute; width: 446px; height: 256px;
    border-radius: 16px; overflow: hidden;
    box-shadow: 0 6px 18px rgba(0,0,0,.45);
  }
  .card--light { background: linear-gradient(160deg, #ffffff, var(--card-light) 60%, var(--card-light-edge)); color: var(--ink-dark); }
  .card--dark  { background: linear-gradient(160deg, var(--card-dark-edge), var(--card-dark) 55%, #262626); color: var(--ink-light); }

  .front-light { left: 144px; top: 112px; }
  .front-dark  { left: 619px; top: 110px; }
  .back-dark   { left: 149px; top: 400px; }
  .back-light  { left: 612px; top: 400px; }

  .brand { position: absolute; left: 22px; top: 30px; display: flex; align-items: center; gap: 12px; }
  .brand__dot { width: 44px; height: 44px; border-radius: 50%; background: var(--mark-grey); }
  .brand__name { font-size: 24px; font-weight: 700; letter-spacing: -.3px; }
  .card--light .brand__name { color: var(--ink-dark); }
  .card--dark .brand__name { color: var(--ink-light); }

  .person { position: absolute; right: 22px; top: 100px; text-align: right; }
  .person__name { color: var(--brand-green); font-size: 14px; font-weight: 700; line-height: 18px; }
  .person__role { font-size: 12px; line-height: 16px; }

  .accent-bar { position: absolute; left: 0; top: 140px; width: 8px; height: 70px; background: var(--brand-green); }

  .contact { position: absolute; left: 22px; top: 160px; font-size: 10.5px; line-height: 15px; white-space: nowrap; }
  .contact__label { color: var(--brand-green); }
  .contact__sep { color: var(--brand-green); padding: 0 4px; }

  .back-mark {
    position: absolute; left: 0; right: 0; top: 106px;
    display: flex; align-items: center; justify-content: center; gap: 12px;
  }
  .back-mark__dot { width: 44px; height: 44px; border-radius: 50%; background: var(--mark-grey); }
  .back-mark__name { font-size: 22px; font-weight: 700; color: var(--mark-grey); }
  .back-url { position: absolute; left: 0; right: 0; bottom: 12px; text-align: center; font-size: 10px; color: var(--ink-muted); }
</style>
</head>
<body>
<main class="sheet">

  <section class="card card--light front-light" aria-label="Business card front, light">
    <div class="brand"><span class="brand__dot"></span><span class="brand__name">Kestrel Forge Tech</span></div>
    <div class="person"><div class="person__name">Wendell Pask</div><div class="person__role">Owner</div></div>
    <div class="accent-bar"></div>
    <div class="contact">
      <div>218 Larkspur Avenue Suite 4400, Harlow Bend, OR 97915</div>
      <div><span class="contact__label">Phone :</span> 503.555.0148<span class="contact__sep">|</span><span class="contact__label">Cell :</span> 503.555.0163</div>
      <div><span class="contact__label">Fax :</span> 503.555.0172<span class="contact__sep">|</span><span class="contact__label">Email :</span> Wendell.Pask@kestrelforgetech.com</div>
      <div><span class="contact__label">Web :</span> www.kestrelforgetech.com</div>
    </div>
  </section>

  <section class="card card--dark front-dark" aria-label="Business card front, dark">
    <div class="brand"><span class="brand__dot"></span><span class="brand__name">Kestrel Forge Tech</span></div>
    <div class="person"><div class="person__name">Wendell Pask</div><div class="person__role">Owner</div></div>
    <div class="accent-bar"></div>
    <div class="contact">
      <div>218 Larkspur Avenue Suite 4400, Harlow Bend, OR 97915</div>
      <div><span class="contact__label">Phone :</span> 503.555.0148<span class="contact__sep">|</span><span class="contact__label">Cell :</span> 503.555.0163</div>
      <div><span class="contact__label">Fax :</span> 503.555.0172<span class="contact__sep">|</span><span class="contact__label">Email :</span> Wendell.Pask@kestrelforgetech.com</div>
      <div><span class="contact__label">Web :</span> www.kestrelforgetech.com</div>
    </div>
  </section>

  <section class="card card--dark back-dark" aria-label="Business card back, dark">
    <div class="back-mark"><span class="back-mark__dot"></span><span class="back-mark__name">Kestrel Forge Tech</span></div>
    <div class="back-url">www.kestrelforgetech.com</div>
  </section>

  <section class="card card--light back-light" aria-label="Business card back, light">
    <div class="back-mark"><span class="back-mark__dot"></span><span class="back-mark__name">Kestrel Forge Tech</span></div>
    <div class="back-url">www.kestrelforgetech.com</div>
  </section>

</main>
</body>
</html>
```